Looking to get a signage design to be put infront of our store/building.

We need a design of our building with an existing Logo ( uploads inc).

We sell stainless steel sinks and benches as our main line of business.
We also sell Cool Room Shelving, Chrome Wire Shelving, Shop Fittings and Wardrobe Solutions and need the building to reflect this.

We would like to include our Logo and note that the font of the building will require painting to best reflect our crisp clean logo.

I have attached our brochure so you can get a feel for who we are. We do not manufacture so items are here ready to go

Target Market(s)

Cafe and restaurant owners, medical industry, domestic kitchens

Font styles to use
Other font styles liked:
• Minimo font used

Colors
0054AA
0677BA
7BADD7
CADEEF
E8F1F8

Requirements
Nice to have
• Would possibly be nice to see some of our products in our brochure on the building

```html
<!DOCTYPE html>
<html lang="en">
<head>
<meta charset="utf-8">
<title>Clearline Stainless – Storefront Sign</title>
<link href="https://fonts.googleapis.com/css2?family=Arimo:wght@400;700&display=swap" rel="stylesheet">
<style>
  :root {
    --brand-blue: #1e94d3;
    --sign-white: #ffffff;
    --sign-charcoal: #37383c;
    --text-light: #f2f4f6;
    --page-bg: #e9ebee;
    --steel-light: #c9ced3;
    --steel-dark: #8e959c;
  }
  * { box-sizing: border-box; margin: 0; padding: 0; }
  html, body {
    width: 1200px;
    height: 799px;
    overflow: hidden;
    background: var(--page-bg);
    font-family: "Arimo", Arial, sans-serif;
  }
  .sign {
    position: absolute;
    left: 40px;
    top: 195px;
    width: 1120px;
    height: 410px;
    box-shadow: 0 6px 18px rgba(0,0,0,0.18);
  }
  .sign__header {
    position: absolute;
    left: 0; top: 0;
    width: 100%;
    height: 192px;
    background: var(--sign-white);
  }
  .brand {
    position: absolute;
    left: 333px;
    top: 41px;
    width: 450px;
    height: 132px;
    display: flex;
    align-items: center;
    justify-content: center;
    gap: 18px;
  }
  .brand__square {
    width: 26px;
    height: 26px;
    background: var(--brand-blue);
  }
  .brand__name {
    font-family: "Arimo", Arial, sans-serif;
    font-weight: 400;
    font-size: 34px;
    color: var(--brand-blue);
    letter-spacing: 0.5px;
  }
  .sign__body {
    position: absolute;
    left: 0; top: 192px;
    width: 100%;
    height: 218px;
    background: var(--sign-charcoal);
  }
  .offer {
    position: absolute;
    left: 191px;
    top: 22px;
    width: 736px;
    height: 155px;
    border: 2px solid var(--brand-blue);
  }
  .offer__headline {
    height: 46px;
    background: var(--brand-blue);
    color: var(--sign-white);
    font-weight: 700;
    font-size: 28px;
    line-height: 46px;
    text-align: center;
    letter-spacing: 0.2px;
  }
  .offer__list {
    position: absolute;
    left: 0; right: 0;
    top: 62px;
    list-style: none;
    color: var(--text-light);
    font-size: 16.5px;
    text-align: center;
    line-height: 31px;
  }
  .offer__list li { display: inline-block; margin: 0 12px; }
  .offer__list li::before { content: "•"; margin-right: 22px; }
  .offer__row { display: block; }
  .product {
    position: absolute;
    background: linear-gradient(180deg, var(--steel-light), var(--steel-dark));
    opacity: 0.85;
  }
  .product--bench { left: 31px; top: 72px; width: 93px; height: 62px; }
  .product--rack { left: 630px; top: 58px; width: 57px; height: 86px; }
</style>
</head>
<body>
  <div class="sign">
    <header class="sign__header">
      <div class="brand">
        <span class="brand__square"></span>
        <span class="brand__name">clearline stainless</span>
      </div>
    </header>
    <section class="sign__body">
      <div class="offer">
        <h1 class="offer__headline">WE SELL STAINLESS STEEL SINKS AND BENCHES</h1>
        <div class="product product--bench" role="img" aria-label="Stainless steel bench with shelves"></div>
        <ul class="offer__list">
          <span class="offer__row"><li>COOL ROOM SHELVING</li><li>CHROME WIRE SHELVING</li></span>
          <span class="offer__row"><li>SHOP FITTINGS</li><li>WARDROBE SOLUTIONS</li></span>
        </ul>
        <div class="product product--rack" role="img" aria-label="Chrome wire shelving unit on castors"></div>
      </div>
    </section>
  </div>
</body>
</html>
```